Crestwell Advisory Services

I'm looking to create a flyer for my business to provide a consultant service. I will be providing the following below
Launch Your Business Today for only $150
(state fee not included)
Business Formation includes:
*Limited liability Corporation (LLC)
*Halvers and Quint Number
*FEIN
*Operation Agreement for partnership LLCs (For 2 or more member(s)
*Commercial Activity license (If needed for your Business )
*Same -day turnaround service with documents
Schedule your Appointment today
Call or text:318-472-6051
Email:MoralesCapitalCircle@fernmail.net
Target Market(s)
I want the flyer to attract people who wants to start a business but doesn’t know where to start. I want the flyer to stand out form the other consultant businesses.
Industry/Entity Type
Consultant
Requirements
Must have
- The State fee not included should be in small print
Highlight the price or service
Highlight the phrase "launch you business today"
Nice to have
- Different samples of colors, a variety
Should not have
- should not be all one color

```html
<!DOCTYPE html>
<html lang="en">
<head>
<meta charset="utf-8">
<title>Crestwell Advisory Services – Launch Your Business Today</title>
<link rel="stylesheet" href="https://fonts.googleapis.com/css2?family=Montserrat:wght@500;600;700;800&family=Signika:wght@400;500&display=swap">
<style>
  :root {
    --stage: #ebe5de;
    --paper: #ffffff;
    --navy: #0d4868;
    --ink: #111111;
    --orange: #f26a21;
    --orange-light: #f5882a;
    --red-orange: #ee4a2a;
    --photo-light: #c9b7a4;
    --photo-mid: #8d6f58;
    --photo-dark: #3b2b22;
  }
  * { box-sizing: border-box; margin: 0; padding: 0; }
  html, body { width: 1200px; height: 800px; overflow: hidden; }
  body { background: var(--stage); position: relative; }

  .flyer {
    position: absolute;
    left: 305px; top: 20px;
    width: 890px; height: 1147px;
    transform: scale(0.6625);
    transform-origin: top left;
    background: var(--paper);
    overflow: hidden;
    box-shadow: 0 10px 30px rgba(0,0,0,0.18);
    font-family: 'Signika', sans-serif;
  }
  .flyer-art { position: absolute; inset: 0; }

  .headline {
    position: absolute; left: 33px; top: 172px;
    font-family: 'Montserrat', sans-serif;
    color: var(--paper);
    line-height: 1;
  }
  .headline-line { display: block; font-weight: 600; font-size: 70px; letter-spacing: -1px; }
  .headline-accent { display: block; font-weight: 800; font-size: 96px; color: var(--orange); letter-spacing: -2px; margin: 6px 0 4px; }

  .offer {
    position: absolute; left: 0; top: 675px; width: 450px;
    text-align: center; color: var(--navy);
  }
  .offer-lead { font-family: 'Montserrat', sans-serif; font-weight: 500; font-size: 74px; letter-spacing: -1px; line-height: 1; }
  .offer-price { font-family: 'Montserrat', sans-serif; font-weight: 800; font-size: 82px; line-height: 1; margin-top: 14px; }
  .offer-note { font-size: 18px; margin-top: 14px; }

  .services { position: absolute; left: 458px; top: 580px; width: 420px; color: var(--ink); }
  .services-title { font-family: 'Montserrat', sans-serif; font-weight: 700; font-size: 23px; margin-bottom: 24px; }
  .services-list { list-style: none; }
  .services-list li {
    position: relative; padding-left: 25px;
    font-size: 22px; line-height: 27px; margin-bottom: 14px;
  }
  .services-list li::before {
    content: ""; position: absolute; left: 0; top: 9px;
    width: 12px; height: 12px; border-radius: 50%; background: var(--ink);
  }
  .services-list li.tall { margin-bottom: 20px; }

  .cta {
    position: absolute; left: 0; right: 0; top: 990px;
    text-align: center;
    font-family: 'Montserrat', sans-serif; font-weight: 700;
    font-size: 20px; color: var(--navy);
  }

  .contact-bar {
    position: absolute; left: 0; right: 0; bottom: 0; height: 120px;
    background: linear-gradient(90deg, var(--red-orange), var(--orange) 55%, var(--orange-light));
    color: var(--paper);
    font-family: 'Montserrat', sans-serif;
  }
  .community { position: absolute; left: 21px; top: 36px; font-size: 19px; line-height: 25px; font-weight: 500; }
  .contact-line { position: absolute; left: 400px; display: flex; align-items: center; gap: 12px; font-size: 21px; font-weight: 500; }
  .contact-line.phone { top: 20px; }
  .contact-line.email { top: 68px; }
  .contact-line small { font-size: 17px; }
  .contact-icon { width: 36px; height: 36px; flex: none; }
</style>
</head>
<body>
  <main class="flyer">
    <svg class="flyer-art" viewBox="0 0 890 1147" width="890" height="1147">
      <defs>
        <linearGradient id="photoTone" x1="0" y1="0" x2="1" y2="1">
          <stop offset="0" stop-color="#d8cbbd"/>
          <stop offset="0.45" stop-color="#a88a72"/>
          <stop offset="1" stop-color="#3b2b22"/>
        </linearGradient>
        <linearGradient id="wedgeLeft" x1="0" y1="0" x2="1" y2="1">
          <stop offset="0" stop-color="#f47a26"/>
          <stop offset="1" stop-color="#e8432a"/>
        </linearGradient>
        <linearGradient id="wedgeRight" x1="0" y1="1" x2="1" y2="0">
          <stop offset="0" stop-color="#f7942c"/>
          <stop offset="1" stop-color="#ef4f2b"/>
        </linearGradient>
      </defs>
      <rect class="hero-photo" x="0" y="0" width="890" height="640" fill="url(#photoTone)" role="img" aria-label="Photo of two smiling business partners reviewing a phone together in a warmly lit lounge"/>
      <polygon class="band-left" points="0,385 335,560 335,612 0,482" fill="url(#wedgeLeft)"/>
      <polygon class="band-right" points="210,568 890,280 890,383 330,612" fill="url(#wedgeRight)"/>
      <polygon class="content-field" points="0,482 330,612 890,383 890,1147 0,1147" fill="#ffffff"/>
    </svg>

    <h1 class="headline">
      <span class="headline-line">LAUNCH YOUR</span>
      <span class="headline-accent">BUSINESS</span>
      <span class="headline-line">TODAY</span>
    </h1>

    <section class="offer">
      <p class="offer-lead">FOR ONLY</p>
      <p class="offer-price">$150</p>
      <p class="offer-note">(state fee not included)</p>
    </section>

    <section class="services">
      <h2 class="services-title">BUSINESS FORMATION INCLUDES:</h2>
      <ul class="services-list">
        <li>Limited liability Corporation (LLC)</li>
        <li>Halvers and Quint Number</li>
        <li>FEIN</li>
        <li class="tall">Operation Agreement for partnership LLCs (For 2 or more member(s)</li>
        <li class="tall">Commercial Activity license<br>(If needed for your Business )</li>
        <li>Same -day turnaround service<br>with documents</li>
      </ul>
    </section>

    <p class="cta">SCHEDULE YOUR APPOINTMENT TODAY</p>

    <footer class="contact-bar">
      <p class="community">To Join With<br>Our Community</p>
      <p class="contact-line phone">
        <svg class="contact-icon" viewBox="0 0 24 24" aria-hidden="true"><path fill="#fff" d="M6.6 10.8a15.1 15.1 0 0 0 6.6 6.6l2.2-2.2a1 1 0 0 1 1-.25 11.4 11.4 0 0 0 3.6.57 1 1 0 0 1 1 1V20a1 1 0 0 1-1 1A17 17 0 0 1 3 4a1 1 0 0 1 1-1h3.5a1 1 0 0 1 1 1c0 1.25.2 2.45.57 3.57a1 1 0 0 1-.25 1z"/></svg>
        <span>318-472-6051 <small>(Call or text)</small></span>
      </p>
      <p class="contact-line email">
        <svg class="contact-icon" viewBox="0 0 24 24" aria-hidden="true"><rect x="2" y="5" width="20" height="14" fill="none" stroke="#fff" stroke-width="2"/><path d="M2 5l10 8 10-8" fill="none" stroke="#fff" stroke-width="2"/></svg>
        <span>MoralesCapitalCircle@fernmail.net</span>
      </p>
    </footer>
  </main>
</body>
</html>
```